Calendar Ad / Flyer

Our law firm needs a calendar ad to place in a local calendar.
THE DEADLINE IS THIS THURSDAY 06/28/2018.

Attached is the ad used in last years calendar. A few notes on this...
**. This is by no means the model to follow.
Please be creative and do what makes more sense marketing wise.
1. Need to update the color scheme which corresponds to the new website at morvanlegal.net
2. The "MORVAN LEGAL | STANDING FIRM FOR YOUR FUTURE" should be put at the top and made larger
3. "KNOWN AND TRUSTED IN OUR COMMUNITY FOR OVER 21 YEARS" should be changed to "KNOWN AND TRUSTED IN OUR COMMUNITY FOR OVER 22 YEARS"
4. "Dorian K. Morvan, Esq." should be made larger and better positioned.
5. Under the list of practices, it should be changed to have:
"Personal Injury, Legal Malpractice, Unlicensed Contractors, Medical Malpractice, Civil Litigation"
6. Contact information (i.e. contact number, website, and address) should be better positioned
7. Placement of endorsement logos should stand out more.
8. New picture of head attorney is attached.

Last but not least... Give it your best shot!

```html
<!DOCTYPE html>
<html lang="en">
<head>
<meta charset="utf-8">
<title>Morvan Legal – Calendar Ad</title>
<link rel="stylesheet" href="https://fonts.googleapis.com/css2?family=Lato:wght@400;700;900&display=swap">
<style>
  :root {
    --gold: #c9a46c;
    --gold-dark: #b8915a;
    --ink: #2f2f31;
    --charcoal: #333335;
    --panel: #d4d4d6;
    --text-gray: #444446;
    --white: #ffffff;
    --photo-light: #eeeeef;
    --photo-mid: #a9a9ad;
    --photo-dark: #55565a;
  }
  * { margin: 0; padding: 0; box-sizing: border-box; }
  html, body { width: 1200px; height: 900px; overflow: hidden; background: var(--white); }
  .ad {
    position: relative;
    width: 1200px;
    height: 900px;
    overflow: hidden;
    background: var(--white);
    font-family: "Lato", Arial, sans-serif;
    color: var(--ink);
  }
  .ad-shapes { position: absolute; inset: 0; }
  .attorney-photo {
    position: absolute;
    left: 515px; top: 0;
    width: 685px; height: 499px;
    background: linear-gradient(180deg, var(--photo-light) 0%, var(--photo-mid) 55%, var(--photo-dark) 100%);
    clip-path: polygon(22% 100%, 32% 40%, 50% 0, 100% 0, 100% 100%);
  }
  .brand {
    position: absolute;
    left: 58px; top: 150px;
    display: flex; align-items: center; gap: 18px;
  }
  .brand-mark { width: 34px; height: 34px; background: var(--gold); }
  .brand-name {
    font-weight: 900;
    font-size: 64px;
    letter-spacing: 5px;
    color: var(--gold);
    line-height: 1;
  }
  .brand-tagline {
    position: absolute;
    left: 210px; top: 224px;
    font-weight: 700;
    font-size: 21px;
    letter-spacing: 1px;
    color: var(--text-gray);
  }
  .trust-line {
    position: absolute;
    left: 83px; top: 365px;
    font-size: 22px;
    line-height: 30px;
    color: var(--ink);
    text-transform: uppercase;
  }
  .practice-list {
    position: absolute;
    left: 96px; top: 532px;
    list-style: none;
  }
  .practice-list li {
    display: flex; align-items: center;
    height: 46.5px;
    font-size: 29px;
    color: var(--text-gray);
  }
  .practice-list svg { width: 16px; height: 18px; margin-right: 22px; }
  .attorney-name {
    position: absolute;
    left: 700px; top: 525px; width: 420px;
    text-align: center;
    font-weight: 700;
    font-size: 32px;
    color: var(--white);
  }
  .contact {
    position: absolute;
    left: 846px; top: 648px;
  }
  .contact-row {
    display: flex; align-items: center;
    height: 50px;
    font-weight: 700;
    font-size: 31px;
    color: var(--charcoal);
  }
  .contact-row svg { width: 24px; height: 26px; margin-right: 12px; }
  .address {
    position: absolute;
    left: 902px; top: 800px;
    font-weight: 700;
    font-size: 17px;
    line-height: 28px;
    color: var(--charcoal);
  }
</style>
</head>
<body>
<main class="ad">
  <svg class="ad-shapes" width="1200" height="900" viewBox="0 0 1200 900" aria-hidden="true">
    <rect class="trust-band" x="0" y="315" width="1200" height="184" fill="var(--gold)"/>
    <polygon class="practice-panel" points="0,499 580,499 806,779 0,779" fill="var(--panel)"/>
    <polygon class="address-panel" points="837,785 1200,785 1200,868 880,868" fill="var(--panel)"/>
    <polygon class="footer-bar" points="0,878 890,878 910,897 0,897" fill="var(--panel)"/>
    <!-- endorsement badges -->
    <g class="badges">
      <circle cx="161" cy="834" r="34" fill="#7a1d1d"/>
      <circle cx="161" cy="834" r="26" fill="none" stroke="var(--gold)" stroke-width="2"/>
      <rect x="244" y="808" width="74" height="52" fill="#d32323"/>
      <rect x="370" y="806" width="70" height="56" rx="4" fill="var(--gold-dark)"/>
      <rect x="480" y="814" width="106" height="40" rx="3" fill="#1b5e97"/>
      <circle cx="668" cy="832" r="32" fill="#ffffff" stroke="#3a8fd6" stroke-width="5"/>
      <rect x="630" y="852" width="76" height="16" fill="#3a8fd6"/>
    </g>
  </svg>

  <div class="attorney-photo" role="img" aria-label="Portrait of attorney Dorian K. Morvan in a grey suit"></div>

  <svg class="ad-shapes" width="1200" height="900" viewBox="0 0 1200 900" aria-hidden="true">
    <polygon class="name-bar" points="619,499 1200,499 1200,587 691,587" fill="var(--charcoal)"/>
  </svg>

  <div class="brand">
    <span class="brand-mark"></span>
    <span class="brand-name">MORVAN LEGAL</span>
  </div>
  <p class="brand-tagline">STANDING FIRM FOR YOUR FUTURE</p>

  <p class="trust-line">Known and trusted in our community<br>for over 22 years</p>

  <ul class="practice-list">
    <li><svg viewBox="0 0 16 18"><path d="M2 1 L14 9 L2 17 L6 9 Z" fill="var(--gold)"/></svg>Personal Injury</li>
    <li><svg viewBox="0 0 16 18"><path d="M2 1 L14 9 L2 17 L6 9 Z" fill="var(--gold)"/></svg>Legal Malpractice</li>
    <li><svg viewBox="0 0 16 18"><path d="M2 1 L14 9 L2 17 L6 9 Z" fill="var(--gold)"/></svg>Unlicensed Contractors</li>
    <li><svg viewBox="0 0 16 18"><path d="M2 1 L14 9 L2 17 L6 9 Z" fill="var(--gold)"/></svg>Medical Malpractice</li>
    <li><svg viewBox="0 0 16 18"><path d="M2 1 L14 9 L2 17 L6 9 Z" fill="var(--gold)"/></svg>Civil Litigation</li>
  </ul>

  <p class="attorney-name">Dorian K. Morvan, Esq.</p>

  <div class="contact">
    <div class="contact-row">
      <svg viewBox="0 0 24 26"><path d="M6 2 C3 3 2 6 3 10 C5 17 10 22 16 24 C19 25 21 23 22 21 L18 17 L15 19 C12 17 9 14 8 11 L10 8 Z" fill="var(--gold)"/></svg>
      (888) 555-0147
    </div>
    <div class="contact-row">
      <svg viewBox="0 0 24 26"><g fill="none" stroke="var(--gold)" stroke-width="1.6"><circle cx="12" cy="13" r="10"/><ellipse cx="12" cy="13" rx="4.5" ry="10"/><line x1="2" y1="13" x2="22" y2="13"/><line x1="4" y1="8" x2="20" y2="8"/><line x1="4" y1="18" x2="20" y2="18"/></g></svg>
      morvanlegal.net
    </div>
  </div>

  <p class="address">2180 Linden Ave. | Suite 410<br>Fairmont, CA | 90299</p>
</main>
</body>
</html>
```